Design business cards for Ironvale Barbers (Opening March so won't need finalised till January2018

Ironvale Barbers is the new age barbers and skincare for all men. Creating tailor made haircuts & customised skincare solutions for the perfect healthy manly look. The Barbers will have a industrial, rustic, worldly feel about it. Rustic red brick wall with old wine barrels as the work stations with the old fashion barber chairs. Concrete floor and a bit corrugated iron around.
Target Market(s)
Professional males who like a great haircut, wet shave and may consider a facial if in the right environment. Total pampering experience in a boys environment.
Industry/Entity Type
Barber
Contact Information for Business Card
Front- Logo - address is 42 Kowhai Rd Taupo
Ph - (07) 348 6192
www.ironvalebarbers.com
email - hello@ironvale.co.nz
Back of card
Mens Haircare - Wet Shaving - Facials - Skin Prescriptions
We are doing a loyalty program - 6 squares numbered then 7th free
Colors
Designer to choose colors to be used in the design.
Requirements
Must have
- Clean simple easy to read.
Nice to have
- Our current colours are white font on black background but thinking we need to introduce another colour. Maybe white logo on a copper, bronze or rusty background. Or even a rustic red brick wall with white writing. Want it clean simple to read. Maybe a burgundy?
Should not have
- no images like heads, scissors, razors please

```html
<!DOCTYPE html>
<html lang="en">
<head>
<meta charset="utf-8">
<title>Ironvale Barbers – Business Cards</title>
<link rel="stylesheet" href="https://fonts.googleapis.com/css2?family=Oswald:wght@400;500&family=Arvo:wght@400&family=Playfair+Display:wght@700;900&display=swap">
<style>
  :root {
    --page: #e9e4dc;
    --card-black: #0b0b0b;
    --ink-light: #d9d9d9;
    --ink-white: #f2f2f2;
    --panel-grey: #c9c9cb;
    --brick-dark: #7a3524;
    --brick-mid: #a8503a;
    --brick-light: #c0664a;
    --mortar: #8d7f74;
  }
  * { box-sizing: border-box; margin: 0; padding: 0; }
  html, body { width: 1200px; height: 800px; overflow: hidden; }
  body {
    background: var(--page);
    display: flex;
    align-items: center;
    justify-content: center;
    gap: 50px;
  }
  .card {
    width: 525px;
    height: 300px;
    position: relative;
    overflow: hidden;
    box-shadow: 0 6px 18px rgba(0,0,0,.18);
  }

  /* Loyalty / services side */
  .card--loyalty { background: var(--panel-grey); }
  .brick-wall {
    position: absolute; inset: 0 0 auto 0; height: 190px;
    background:
      radial-gradient(ellipse at 30% 40%, var(--brick-light), transparent 60%),
      linear-gradient(135deg, var(--brick-mid), var(--brick-dark) 70%, var(--mortar));
  }
  .brand {
    position: absolute; top: 62px; left: 0; right: 0;
    text-align: center;
    font-family: "Playfair Display", Georgia, serif;
    font-weight: 900;
    color: var(--card-black);
    font-size: 50px;
    letter-spacing: 1px;
    line-height: 1;
    text-transform: uppercase;
  }
  .brand__sub {
    display: block;
    font-size: 20px;
    letter-spacing: 9px;
    margin-top: 6px;
  }
  .services-band {
    position: absolute; top: 190px; left: 0; right: 0; height: 36px;
    background: var(--card-black);
    color: var(--ink-light);
    font-family: "Oswald", "Arial Narrow", sans-serif;
    font-size: 15px;
    letter-spacing: .6px;
    text-transform: uppercase;
    display: flex; align-items: center; justify-content: center;
  }
  .date-field {
    position: absolute; left: 28px; right: 40px; top: 250px;
    display: flex; align-items: flex-end; gap: 10px;
    font-family: "Oswald", "Arial Narrow", sans-serif;
    font-weight: 500; font-size: 15px; color: var(--card-black);
  }
  .date-field__line { flex: 1; border-bottom: 1.5px solid var(--card-black); margin-bottom: 4px; }

  /* Contact side */
  .card--contact {
    background: var(--card-black);
    color: var(--ink-light);
    font-family: "Arvo", "Rockwell", serif;
  }
  .contact-phone { position: absolute; top: 26px; left: 30px; font-size: 16px; letter-spacing: .5px; }
  .contact-rule { position: absolute; top: 44px; left: 190px; width: 140px; height: 1.5px; background: var(--ink-light); }
  .contact-email { position: absolute; top: 62px; right: 30px; font-size: 16px; }
  .person {
    position: absolute; top: 108px; left: 0; right: 0; text-align: center;
  }
  .person__name {
    font-family: "Playfair Display", Georgia, serif;
    font-weight: 700;
    font-size: 48px;
    color: var(--ink-white);
    letter-spacing: 1px;
    line-height: 1;
    transform: scaleY(1.12);
  }
  .person__role {
    display: flex; align-items: center; justify-content: center; gap: 12px;
    margin-top: 8px;
    font-size: 19px; letter-spacing: 2px; text-transform: uppercase;
    font-weight: 400;
  }
  .person__role::before, .person__role::after {
    content: ""; width: 55px; height: 1.5px; background: var(--ink-light);
  }
  .contact-footer {
    position: absolute; bottom: 26px; left: 30px; right: 30px;
    display: flex; justify-content: space-between; align-items: center;
    font-size: 15px; letter-spacing: .5px;
  }
  .contact-footer__divider { width: 1.5px; height: 16px; background: var(--ink-light); }
  .contact-footer__address { text-transform: uppercase; }
</style>
</head>
<body>
  <section class="card card--loyalty">
    <div class="brick-wall" role="img" aria-label="Photograph of a rustic red brick wall"></div>
    <h1 class="brand">Ironvale<span class="brand__sub">Barbers</span></h1>
    <p class="services-band">Men's Haircare - Wet Shaving - Facials - Skin Prescriptions</p>
    <div class="date-field"><span>DATE</span><span class="date-field__line"></span></div>
  </section>

  <section class="card card--contact">
    <p class="contact-phone">(07) 348 6192</p>
    <span class="contact-rule"></span>
    <p class="contact-email">hello@ironvale.co.nz</p>
    <div class="person">
      <h2 class="person__name">LOREM IPSUM</h2>
      <p class="person__role">Manager</p>
    </div>
    <p class="contact-footer">
      <span>www.ironvalebarbers.com</span>
      <span class="contact-footer__divider"></span>
      <span class="contact-footer__address">42 Kowhai Rd Taupo</span>
    </p>
  </section>
</body>
</html>
```